Adult Residential Care Provider (Assisted Living) needs a brochure design.

We need a brochure designed for our assisted living facilites in Metairie (adjacent to New Orleans) called Willowmere Senior Homes. We provide adults, typically Seniors, a place to live where they receive 24-hour care/support of their daily living activities, including laundering, cooking, cleaning, grooming, bathing, etc.. I'd like to use our logo and the color choices should be soft and convey comfort. I would also like the brochure to be editable by my administration to make any changes in the future.

```html
<!DOCTYPE html>
<html lang="en">
<head>
<meta charset="utf-8">
<title>Willowmere Senior Homes – Assisted Living Flyer</title>
<link rel="stylesheet" href="https://fonts.googleapis.com/css2?family=Montserrat:wght@300;400;500;600;700;800&display=swap">
<style>
  :root {
    --teal-deep: #0a5f55;
    --teal: #0c7366;
    --teal-bright: #10897a;
    --cream: #f5efe4;
    --ink: #1d2727;
    --white: #ffffff;
    --backdrop: #dcdcdc;
  }
  * { box-sizing: border-box; margin: 0; padding: 0; }
  html, body {
    width: 996px; height: 1200px; overflow: hidden;
    background: var(--backdrop);
    font-family: "Montserrat", sans-serif;
  }
  .flyer {
    position: absolute; left: 74px; top: 0;
    width: 848px; height: 1200px;
    background: var(--white); overflow: hidden;
  }
  .flyer-art { position: absolute; inset: 0; }
  .brand {
    position: absolute; left: 32px; top: 26px;
    display: flex; align-items: center; gap: 10px;
    color: var(--teal-deep); font-weight: 600;
  }
  .brand-dot { width: 44px; height: 44px; border-radius: 50%; background: var(--teal-deep); }
  .brand-name { font-size: 30px; letter-spacing: 2px; line-height: 1; }
  .brand-sub { font-size: 15px; letter-spacing: 2.4px; margin-top: 5px; }
  .headline {
    position: absolute; left: 32px; top: 112px;
    font-weight: 800; font-size: 46px; line-height: 49px;
    color: var(--teal-deep); letter-spacing: 0.5px;
  }
  .headline-rule {
    position: absolute; left: 32px; top: 318px;
    width: 327px; height: 3px; background: var(--teal-deep);
  }
  .headline-url {
    position: absolute; left: 32px; top: 330px;
    font-size: 21px; font-weight: 500; letter-spacing: 2.3px; color: var(--teal-deep);
  }
  .services-tab {
    position: absolute; left: 292px; top: 654px; width: 226px; height: 50px;
    background: linear-gradient(180deg, var(--teal-bright), var(--teal));
    border-radius: 25px 25px 0 0;
    color: var(--white); font-weight: 700; font-size: 29px; letter-spacing: 1.5px;
    text-align: center; line-height: 52px;
  }
  .services-rule {
    position: absolute; left: 50px; top: 703px; width: 750px; height: 2px; background: var(--teal);
  }
  .service-list {
    position: absolute; list-style: none;
    font-size: 19.5px; line-height: 24px; color: var(--ink);
  }
  .service-list.col-left { left: 58px; top: 719px; width: 330px; }
  .service-list.col-right { left: 396px; top: 719px; width: 400px; }
  .service-list li { position: relative; padding-left: 33px; }
  .service-list li svg { position: absolute; left: 0; top: 3px; width: 20px; height: 20px; }
  .amenities-bar {
    position: absolute; left: 87px; top: 879px; width: 674px; height: 44px;
    background: var(--teal); border-radius: 22px;
    box-shadow: 0 2px 4px rgba(0,0,0,0.25);
    color: var(--white); font-weight: 300; font-size: 22.5px;
    text-align: center; line-height: 44px; letter-spacing: 0.3px;
  }
  .icon-row { position: absolute; left: 0; top: 940px; width: 848px; height: 82px; }
  .icon-badge {
    position: absolute; width: 82px; height: 82px; border-radius: 50%;
    background: var(--white); border: 2px solid #c8c8c8;
    box-shadow: 0 1px 3px rgba(0,0,0,0.25);
    display: flex; align-items: center; justify-content: center;
  }
  .icon-badge-inner {
    width: 72px; height: 72px; border-radius: 50%; border: 3px solid var(--teal);
    display: flex; align-items: center; justify-content: center;
  }
  .icon-badge svg { width: 46px; height: 46px; }
  .details-label {
    position: absolute; left: 0; width: 848px; top: 1037px; text-align: center;
    font-weight: 700; font-size: 21px; color: var(--teal); letter-spacing: 0.3px;
  }
  .footer-band {
    position: absolute; left: 0; top: 1096px; width: 848px; height: 104px; background: var(--teal);
  }
  .footer-strip {
    position: absolute; left: 0; top: 1167px; width: 848px; height: 22px; background: var(--teal-deep);
    color: var(--white); font-size: 11.5px; font-weight: 500; letter-spacing: 7px;
    text-align: center; line-height: 22px;
  }
  .call-pill {
    position: absolute; left: 211px; top: 1075px; width: 428px; height: 46px;
    background: var(--cream); border-radius: 23px;
    display: flex; align-items: center; justify-content: center; gap: 10px;
    color: var(--teal-deep); font-weight: 700; font-size: 22px; letter-spacing: 0.6px;
  }
  .call-pill svg { width: 32px; height: 32px; }
  .address {
    position: absolute; top: 1129px; display: flex; align-items: center; gap: 12px;
    color: var(--white); font-size: 15.5px; font-weight: 400;
  }
  .address svg { width: 32px; height: 32px; }
  .address.first { left: 77px; }
  .address.second { left: 406px; }
</style>
</head>
<body>
<main class="flyer">
  <svg class="flyer-art" viewBox="0 0 848 1200" width="848" height="1200">
    <defs>
      <linearGradient id="tealSweep" x1="0" y1="0" x2="1" y2="1">
        <stop offset="0" stop-color="#0f8a7c"/>
        <stop offset="1" stop-color="#0a5f55"/>
      </linearGradient>
      <linearGradient id="photoTones" x1="0" y1="0" x2="1" y2="1">
        <stop offset="0" stop-color="#f2ebe2"/>
        <stop offset="0.45" stop-color="#e2d2bf"/>
        <stop offset="1" stop-color="#b59273"/>
      </linearGradient>
      <radialGradient id="handsTones" cx="0.5" cy="0.5" r="0.6">
        <stop offset="0" stop-color="#8a5634"/>
        <stop offset="1" stop-color="#d6955a"/>
      </radialGradient>
    </defs>
    <rect class="cream-field" x="0" y="0" width="848" height="700" fill="var(--cream)"/>
    <path class="white-field" fill="var(--white)"
      d="M0,662 C130,662 230,640 300,600 L300,560 L848,560 L848,1200 L0,1200 Z"/>
    <path class="wave-left" fill="url(#tealSweep)"
      d="M0,365 C70,470 180,560 300,590 L300,600 C230,640 130,662 0,662 Z"/>
    <path class="wave-left-light" fill="#12978a" opacity="0.55"
      d="M0,395 C80,500 190,580 300,605 L300,612 C190,590 90,530 0,470 Z"/>
    <path class="wave-right" fill="url(#tealSweep)"
      d="M390,540 C520,600 680,610 848,598 L848,670 C680,700 520,660 400,580 Z"/>
    <path fill="#0a5f55" opacity="0.7"
      d="M430,575 C560,640 700,650 848,640 L848,652 C700,668 560,655 430,585 Z"/>
    <path class="wave-top" fill="url(#tealSweep)"
      d="M360,410 C450,230 650,95 848,74 L848,112 C660,125 475,235 374,405 Z"/>
    <path role="img" aria-label="Photo of a smiling elderly woman with a caregiver resting a hand on her shoulder"
      fill="url(#photoTones)"
      d="M374,405 C475,235 660,125 848,112 L848,598 C680,610 520,600 420,545 Z"/>
    <circle cx="309" cy="496" r="115" fill="var(--teal-deep)"/>
    <circle role="img" aria-label="Photo of two clasped hands offering support" cx="309" cy="496" r="106" fill="url(#handsTones)"/>
  </svg>

  <div class="brand">
    <span class="brand-dot"></span>
    <div>
      <div class="brand-name">WILLOWMERE</div>
      <div class="brand-sub">SENIOR HOMES</div>
    </div>
  </div>

  <h1 class="headline">ASSISTED<br>LIVING &amp;<br>RESIDENTIAL<br>CARE</h1>
  <div class="headline-rule"></div>
  <div class="headline-url">www.willowmerenola.com</div>

  <div class="services-tab">SERVICES</div>
  <div class="services-rule"></div>

  <ul class="service-list col-left">
    <li><svg viewBox="0 0 20 20"><circle cx="10" cy="10" r="10" fill="var(--teal)"/><path d="M5.5 10.2l3 3 6-6" fill="none" stroke="#fff" stroke-width="2.2" stroke-linecap="round" stroke-linejoin="round"/></svg>24 Hours Care</li>
    <li><svg viewBox="0 0 20 20"><circle cx="10" cy="10" r="10" fill="var(--teal)"/><path d="M5.5 10.2l3 3 6-6" fill="none" stroke="#fff" stroke-width="2.2" stroke-linecap="round" stroke-linejoin="round"/></svg>Assistance with Daily Living Activities</li>
    <li><svg viewBox="0 0 20 20"><circle cx="10" cy="10" r="10" fill="var(--teal)"/><path d="M5.5 10.2l3 3 6-6" fill="none" stroke="#fff" stroke-width="2.2" stroke-linecap="round" stroke-linejoin="round"/></svg>Bathing Assistance</li>
    <li><svg viewBox="0 0 20 20"><circle cx="10" cy="10" r="10" fill="var(--teal)"/><path d="M5.5 10.2l3 3 6-6" fill="none" stroke="#fff" stroke-width="2.2" stroke-linecap="round" stroke-linejoin="round"/></svg>Beauty and Haircare</li>
    <li><svg viewBox="0 0 20 20"><circle cx="10" cy="10" r="10" fill="var(--teal)"/><path d="M5.5 10.2l3 3 6-6" fill="none" stroke="#fff" stroke-width="2.2" stroke-linecap="round" stroke-linejoin="round"/></svg>Laundry</li>
  </ul>
  <ul class="service-list col-right">
    <li><svg viewBox="0 0 20 20"><circle cx="10" cy="10" r="10" fill="var(--teal)"/><path d="M5.5 10.2l3 3 6-6" fill="none" stroke="#fff" stroke-width="2.2" stroke-linecap="round" stroke-linejoin="round"/></svg>Housekeeping</li>
    <li><svg viewBox="0 0 20 20"><circle cx="10" cy="10" r="10" fill="var(--teal)"/><path d="M5.5 10.2l3 3 6-6" fill="none" stroke="#fff" stroke-width="2.2" stroke-linecap="round" stroke-linejoin="round"/></svg>3 Home-Cooked Meals and Snacks - Dietitian Approved</li>
    <li><svg viewBox="0 0 20 20"><circle cx="10" cy="10" r="10" fill="var(--teal)"/><path d="M5.5 10.2l3 3 6-6" fill="none" stroke="#fff" stroke-width="2.2" stroke-linecap="round" stroke-linejoin="round"/></svg>Medication Reminders and Supervision</li>
  </ul>

  <div class="amenities-bar">Accommodation | Laundry | Food | Medication Storage</div>

  <div class="icon-row">
    <div class="icon-badge" style="left:145px"><div class="icon-badge-inner">
      <svg viewBox="0 0 46 46" fill="none" stroke="var(--teal)" stroke-width="2.4" stroke-linecap="round" stroke-linejoin="round">
        <path d="M23 24c-6-4-10-7-10-11a5 5 0 0 1 10-1 5 5 0 0 1 10 1c0 4-4 7-10 11z" fill="var(--teal)"/>
        <path d="M6 26l7 9h9M40 26l-7 9h-9"/>
      </svg></div></div>
    <div class="icon-badge" style="left:264px"><div class="icon-badge-inner">
      <svg viewBox="0 0 46 46" fill="none" stroke="var(--teal)" stroke-width="2.4" stroke-linecap="round">
        <path d="M10 38V18a8 8 0 0 1 16 0" stroke-width="5"/>
        <path d="M20 20l10-6 4 8-12 2z" fill="var(--teal)"/>
        <path d="M30 26l4 6M34 24l6 5M36 20l7 3"/>
      </svg></div></div>
    <div class="icon-badge" style="left:383px"><div class="icon-badge-inner">
      <svg viewBox="0 0 46 46" fill="none" stroke="var(--teal)" stroke-width="2.4" stroke-linecap="round">
        <path d="M7 24h32a16 13 0 0 1-32 0z"/>
        <path d="M16 39h14M10 12l10 10"/>
        <path d="M26 8c2 2-2 4 0 6M32 8c2 2-2 4 0 6M38 8c2 2-2 4 0 6"/>
      </svg></div></div>
    <div class="icon-badge" style="left:503px"><div class="icon-badge-inner">
      <svg viewBox="0 0 46 46" fill="none" stroke="var(--teal)" stroke-width="2.4" stroke-linecap="round" stroke-linejoin="round">
        <rect x="8" y="7" width="30" height="33" rx="3"/>
        <path d="M8 14h30"/>
        <circle cx="21" cy="27" r="8"/>
        <path d="M30 10.5h4"/>
      </svg></div></div>
    <div class="icon-badge" style="left:622px"><div class="icon-badge-inner">
      <svg viewBox="0 0 46 46" fill="none" stroke="var(--teal)" stroke-width="2.4" stroke-linecap="round">
        <circle cx="14" cy="34" r="5"/><circle cx="32" cy="34" r="5"/>
        <path d="M17 30L33 8M29 30L13 8"/>
      </svg></div></div>
  </div>

  <div class="details-label">FOR FURTHER DETAILS</div>

  <div class="footer-band"></div>
  <div class="call-pill">
    <span>CALL US ON</span>
    <svg viewBox="0 0 32 32">
      <circle cx="16" cy="16" r="14" fill="none" stroke="var(--teal-deep)" stroke-width="2.5"/>
      <path d="M11 9.5l3 .5 1 4-2 1.5a10 10 0 0 0 4 4l1.5-2 4 1 .5 3c-1 1.5-3 2-5 1a16 16 0 0 1-8-8c-1-2-.5-4 1-5z" fill="var(--teal-deep)"/>
    </svg>
    <span>(504) 555-0142</span>
  </div>

  <div class="address first">
    <svg viewBox="0 0 32 32" fill="none" stroke="#fff" stroke-width="1.6">
      <circle cx="16" cy="16" r="14.5"/>
      <path d="M16 25c-4-5-6-8-6-11a6 6 0 0 1 12 0c0 3-2 6-6 11z"/><circle cx="16" cy="14" r="2.2"/>
    </svg>
    <span>214 Cypress Ln. Metairie, LA 70005</span>
  </div>
  <div class="address second">
    <svg viewBox="0 0 32 32" fill="none" stroke="#fff" stroke-width="1.6">
      <circle cx="16" cy="16" r="14.5"/>
      <path d="M16 25c-4-5-6-8-6-11a6 6 0 0 1 12 0c0 3-2 6-6 11z"/><circle cx="16" cy="14" r="2.2"/>
    </svg>
    <span>5120 Magnolia Ct. Metairie, LA 70002</span>
  </div>

  <div class="footer-strip">WWW.WILLOWMERENOLA.COM</div>
</main>
</body>
</html>
```